Maple Hollow Campground Billboard

We need an eye-catching, traffic-stopping design for a 15 ft x 10 ft billboard that will be located near the turn-off to our RV park in Colorado. Our park is located on the banks of the Rio Grande River and we want to emphasize that we have shady spots on the river. This is a link to our website www.maplehollowcampground.com and it will give you an idea about our park and what we have to offer. The billboard will be double-sided and face both directions of a busy highway. The park and the river is not visible from the highway, so we want to attract attention.

Target Market(s)

RV travelers on US Hwy 160 in South Fork, Colorado

Font styles to use
Sans Serif

Colors

Designer to choose colors to be used in the design.

Requirements
Must have
• Simple, eye-catching message.
Nice to have
• Incorporate our logo and give directions.
Should not have
• Too much information that can't be read while speeding down a busy highway.

```html
<!DOCTYPE html>
<html lang="en">
<head>
<meta charset="utf-8">
<title>Maple Hollow Campground Billboard</title>
<link rel="stylesheet" href="https://fonts.googleapis.com/css2?family=Bebas+Neue&family=Oswald:wght@500&family=Roboto:wght@700&family=Michroma&display=swap">
<style>
  :root {
    --sky: #dfe7e8;
    --forest: #3f6a2a;
    --meadow: #7fb03a;
    --fairway: #9cc73f;
    --band-dark: #1f94b8;
    --band-light: #5fd0f2;
    --divider: #f2d31b;
    --ink: #1d1d1d;
    --white: #ffffff;
    --yellow: #fff200;
    --blue: #0d8fd8;
    --pink: #e8268f;
    --orange: #f58a2c;
    --red: #e9353a;
    --green: #93c83e;
    --brand-mark: #1f3d1f;
  }
  * { margin: 0; padding: 0; box-sizing: border-box; }
  html, body { width: 1200px; height: 800px; overflow: hidden; background: #fff; }
  .billboard { position: relative; width: 1200px; height: 800px; overflow: hidden; font-family: "Bebas Neue", sans-serif; }
  .scenery {
    position: absolute; inset: 0;
    background: linear-gradient(180deg, var(--sky) 0%, #5e7f4c 10%, var(--forest) 35%, #4f7f2c 60%, var(--meadow) 78%, var(--fairway) 100%);
  }
  .contact-band { position: absolute; left: 0; top: 69px; height: 69px; width: 960px; display: flex; align-items: center;
    background: linear-gradient(90deg, var(--band-dark) 0%, var(--band-dark) 58%, var(--band-light) 62%, var(--band-light) 100%); }
  .website { font-family: "Roboto", sans-serif; font-weight: 700; font-size: 30px; color: var(--white); margin-left: 51px; width: 520px; }
  .divider { width: 2px; height: 44px; background: var(--divider); margin-left: 15px; }
  .phone { font-family: "Oswald", sans-serif; font-weight: 500; font-size: 58px; color: var(--ink); margin-left: 30px; letter-spacing: -1px; }
  .brand { position: absolute; left: 968px; top: 50px; width: 190px; display: flex; align-items: center; gap: 10px; }
  .brand-dot { width: 26px; height: 26px; border-radius: 50%; background: var(--brand-mark); flex: none; }
  .brand-name { font-family: "Bebas Neue", sans-serif; font-size: 34px; line-height: 0.95; color: var(--white); }
  .headline { position: absolute; left: 0; width: 1200px; text-align: center; line-height: 1; }
  .headline-top { top: 178px; font-size: 132px; color: var(--white); letter-spacing: -1px; }
  .headline-bottom { top: 288px; font-size: 132px; color: var(--yellow); letter-spacing: -1px; }
  .offers-label { position: absolute; top: 430px; left: 0; width: 1200px; text-align: center; font-family: "Michroma", sans-serif; font-size: 21px; color: var(--white); letter-spacing: 1px; }
  .offer { position: absolute; height: 64px; display: flex; align-items: center; justify-content: center; font-size: 36px; color: var(--white); }
  .offer-rv { left: 70px; top: 486px; width: 235px; background: var(--blue); }
  .offer-river { left: 325px; top: 486px; width: 261px; background: var(--pink); }
  .offer-tent { left: 606px; top: 486px; width: 168px; background: var(--orange); }
  .offer-fishing { left: 794px; top: 486px; width: 336px; background: var(--red); }
  .offer-amenities { left: 273px; top: 572px; width: 651px; height: 65px; background: var(--green); color: var(--ink); }
</style>
</head>
<body>
  <main class="billboard">
    <div class="scenery" role="img" aria-label="Photo of a green golf course beside the river with forested hills behind"></div>

    <div class="contact-band">
      <span class="website">www.maplehollowcampground.com</span>
      <span class="divider"></span>
      <span class="phone">800 555 0142</span>
    </div>

    <div class="brand">
      <span class="brand-dot"></span>
      <span class="brand-name">Maple Hollow<br>Campground</span>
    </div>

    <h1 class="headline headline-top">MAKE YOUR VISIT</h1>
    <p class="headline headline-bottom">AN ENJOYABLE ONE</p>

    <p class="offers-label">CAMPGROUND OFFERS</p>

    <div class="offer offer-rv">LARGE RV SPACES</div>
    <div class="offer offer-river">RIVERFRONT SPACES</div>
    <div class="offer offer-tent">TENT SITES</div>
    <div class="offer offer-fishing">FISHING ON THE RIO GRANDE</div>
    <div class="offer offer-amenities">ACCESS TO OUR LARGE ARRAY OF CAMPGROUND AMENITIES</div>
  </main>
</body>
</html>
```